QM Candle Tube Packaging Design

Website: www.quorelmaren.com
IG: @quorel.maren
Tagline: Elevate Your Ambiance
My brand is a sophisticated brand with luxury candles made of coconut wax. Im looking for an upscale minimalist chic design.
Discover the transformative power of positive energy with Quorel Maren candles. Indulge in true luxury with our specially crafted coconut wax blend that not only ignites captivating scents but also embodies modern elegance and empowering elements.
At Quorel Maren we're committed to delivering a unique and exhilarating aromatic experience to all candle lovers. Each candle is meticulously handcrafted in small batches using luxury fragrance oils exclusively formulated for coconut wax.
Our candles are:
Clean-burning
Paraben-Free
Phthalate-Free
Skin-Safe
Pet-Friendly

```html
<!DOCTYPE html>
<html lang="en">
<head>
<meta charset="UTF-8">
<title>Quorel Maren — Candle Tube Label</title>
<link rel="stylesheet" href="https://fonts.googleapis.com/css2?family=Italiana&family=Josefin+Sans:wght@400&family=La+Belle+Aurore&family=Great+Vibes&family=Quicksand:wght@500&display=swap">
<style>
  :root {
    --bg: #dde2dc;
    --ink: #1e1e1e;
    --sage: #9cb9a9;
    --slate: #8b9299;
  }
  html, body {
    margin: 0;
    padding: 0;
    overflow: hidden;
    background: var(--bg);
  }
  .label {
    position: relative;
    width: 891px;
    height: 1200px;
    background: var(--bg);
    overflow: hidden;
  }
  .brand-name {
    position: absolute;
    top: 148px;
    left: 0;
    width: 100%;
    text-align: center;
    font-family: "Italiana", serif;
    font-size: 74px;
    letter-spacing: 0.04em;
    color: var(--ink);
    line-height: 1;
    margin: 0;
    font-weight: 400;
  }
  .brand-sub {
    position: absolute;
    top: 257px;
    left: 0;
    width: 100%;
    display: flex;
    justify-content: center;
    align-items: center;
    gap: 18px;
    font-family: "Josefin Sans", sans-serif;
    font-size: 17px;
    letter-spacing: 0.55em;
    color: var(--ink);
  }
  .brand-sub .rule {
    display: block;
    width: 34px;
    height: 1.5px;
    background: var(--ink);
  }
  .brand-sub .words { margin-right: -0.55em; }
  .brand-motto {
    position: absolute;
    top: 292px;
    left: 0;
    width: 100%;
    text-align: center;
    font-family: "La Belle Aurore", cursive;
    font-size: 20px;
    color: var(--ink);
  }
  .tagline {
    position: absolute;
    top: 398px;
    left: 0;
    width: 100%;
    text-align: center;
    font-family: "Great Vibes", cursive;
    font-size: 150px;
    line-height: 160px;
    color: var(--sage);
    margin: 0;
    font-weight: 400;
  }
  .benefits {
    position: absolute;
    top: 834px;
    left: 0;
    width: 100%;
    list-style: none;
    margin: 0;
    padding: 0;
    text-align: center;
    font-family: "Quicksand", sans-serif;
    font-weight: 500;
    font-size: 20px;
    line-height: 45.7px;
    color: var(--slate);
  }
  .net-weight {
    position: absolute;
    top: 1098px;
    left: 0;
    width: 100%;
    text-align: center;
    font-family: "Quicksand", sans-serif;
    font-weight: 500;
    font-size: 20px;
    color: var(--slate);
  }
</style>
</head>
<body>
  <main class="label">
    <h1 class="brand-name">QUOREL MAREN</h1>
    <div class="brand-sub">
      <span class="rule"></span>
      <span class="words">HANDMADE CANDLES</span>
      <span class="rule"></span>
    </div>
    <div class="brand-motto">with purpose and love</div>

    <h2 class="tagline">Elevate Your<br>Ambiance</h2>

    <ul class="benefits">
      <li>CLEAN-BURNING</li>
      <li>PARABEN-FREE</li>
      <li>PHTHALATE-FREE</li>
      <li>SKIN-SAFE</li>
      <li>PET-FRIENDLY</li>
    </ul>

    <div class="net-weight">14OZ. (396G)</div>
  </main>
</body>
</html>
```